Business Card Design

Consultation for design, construction athletic facilities specializing in synthetic turf systems and all weather running track systems.
Motto "True Owner Representation"
New Company that we'd like to highlight the LOGO first and foremost with the colors of the background and font as primary colors of the card too if possible. I've also attached a typical larger project design layout that could be used in the background to highlight our design and construction specialty.
Website is something we want very noticeable for driving traffic.
Target Market(s)
Athletic Directors, Designers, Government and Military, Contractors
Industry/Entity Type
Construction
Contact Information for Business Card
Peter L. Vandrell CFB, CTB
48317 W 63rd Ave
Harlow Ridge, WA 99482
C +1 503.555.0147
O +1 808.555.0182
Peter@fieldlaneco.example
www.fieldlaneco.example

```html
<!DOCTYPE html>
<html lang="en">
<head>
<meta charset="utf-8">
<title>Valtera Sport – Business Card</title>
<link rel="stylesheet" href="https://fonts.googleapis.com/css2?family=Carlito:wght@400;700&display=swap">
<style>
  :root {
    --backdrop: #9a9a9a;
    --card-black: #050505;
    --accent-orange: #f7941d;
    --soft-orange: #e9a55a;
    --paper-white: #ffffff;
    --plan-tint: #f6dcc4;
  }
  * { box-sizing: border-box; margin: 0; padding: 0; }
  html, body { width: 1200px; height: 900px; overflow: hidden; }
  body {
    background: var(--backdrop);
    font-family: "Carlito", "Calibri", sans-serif;
    display: flex;
    align-items: center;
    justify-content: center;
    gap: 40px;
  }
  .card {
    position: relative;
    width: 540px;
    height: 310px;
    background: var(--card-black);
    overflow: hidden;
    box-shadow: 0 6px 18px rgba(0,0,0,0.35);
  }

  /* Brand lockup */
  .brand {
    position: absolute;
    display: flex;
    align-items: center;
    gap: 10px;
    color: var(--soft-orange);
    font-weight: 400;
    letter-spacing: 3px;
    white-space: nowrap;
  }
  .brand-dot {
    border-radius: 50%;
    background: var(--accent-orange);
    flex: none;
  }

  /* Front */
  .front .brand { top: 58px; left: 250px; font-size: 30px; }
  .front .brand-dot { width: 26px; height: 26px; }
  .holder {
    position: absolute;
    top: 128px;
    right: 300px;
    text-align: right;
    color: var(--accent-orange);
  }
  .holder-name { font-size: 27px; font-weight: 700; white-space: nowrap; }
  .holder-title { font-size: 15px; margin-top: 8px; }
  .divider {
    position: absolute;
    top: 150px;
    left: 254px;
    width: 2px;
    height: 70px;
    background: linear-gradient(to bottom, transparent, var(--accent-orange), transparent);
  }
  .contact-lines {
    position: absolute;
    top: 168px;
    left: 272px;
    color: var(--accent-orange);
    font-size: 14px;
    line-height: 19px;
    list-style: none;
  }
  .contact-band {
    position: absolute;
    left: 0; right: 0; bottom: 24px;
    height: 44px;
    background: var(--accent-orange);
    display: flex;
    align-items: center;
    justify-content: space-between;
    padding: 0 40px;
    color: var(--card-black);
    font-size: 16px;
  }
  .band-item { display: flex; align-items: center; gap: 7px; }
  .band-item svg { width: 15px; height: 15px; }
  .band-item.web { font-size: 18px; }

  /* Back */
  .back .brand { top: 14px; left: 205px; font-size: 24px; }
  .back .brand-dot { width: 20px; height: 20px; }
  .plan-band {
    position: absolute;
    left: 0; right: 0;
    top: 62px;
    height: 172px;
    background: var(--paper-white);
  }
  .plan-drawing {
    position: absolute;
    left: 70px; right: 50px; top: 8px; bottom: 8px;
    background: radial-gradient(ellipse at 55% 50%, var(--plan-tint), var(--paper-white) 75%);
  }
  .back .brand.small {
    top: 176px; left: 20px; font-size: 12px; letter-spacing: 2px; gap: 6px;
  }
  .back .brand.small .brand-dot { width: 11px; height: 11px; }
  .back-site {
    position: absolute;
    right: 40px;
    bottom: 28px;
    color: var(--accent-orange);
    font-size: 17px;
  }
</style>
</head>
<body>

  <section class="card front">
    <div class="brand"><span class="brand-dot"></span>Valtera Sport</div>

    <div class="holder">
      <div class="holder-name">Peter L. Vandrell</div>
      <div class="holder-title">CFB, CTB</div>
    </div>

    <div class="divider"></div>

    <ul class="contact-lines">
      <li>C +1 503.555.0147</li>
      <li>O +1 808.555.0182</li>
      <li>48317 W 63rd Ave Harlow Ridge, WA 99482</li>
    </ul>

    <div class="contact-band">
      <span class="band-item">
        <svg viewBox="0 0 16 16" aria-hidden="true"><rect x="1" y="3" width="14" height="10" fill="none" stroke="currentColor" stroke-width="1.4"/><path d="M1 3 L8 9 L15 3" fill="none" stroke="currentColor" stroke-width="1.4"/></svg>
        Peter@fieldlaneco.example
      </span>
      <span class="band-item web">
        <svg viewBox="0 0 16 16" aria-hidden="true"><circle cx="8" cy="8" r="6.5" fill="none" stroke="currentColor" stroke-width="1.4"/><ellipse cx="8" cy="8" rx="3" ry="6.5" fill="none" stroke="currentColor" stroke-width="1.2"/><path d="M1.5 8 H14.5" stroke="currentColor" stroke-width="1.2"/></svg>
        www.fieldlaneco.example
      </span>
    </div>
  </section>

  <section class="card back">
    <div class="brand"><span class="brand-dot"></span>Valtera Sport</div>
    <div class="plan-band">
      <div class="plan-drawing" role="img" aria-label="Faint site plan of an athletic facility with running track and ball fields"></div>
    </div>
    <div class="brand small"><span class="brand-dot"></span>Valtera Sport</div>
    <div class="back-site">www.fieldlaneco.example</div>
  </section>

</body>
</html>
```